New Bicycle shop business card

Hi!
I'm looking for a business card for my new proffesional bike mechanics shop. This shop is only for fixing broken bikes and not selling bikes.
Peferbly a modern and sleek and modern design.
Colors: black, grey, red, white
Information:
Name: Rijwielwerkplaats Vanhoutem
Shop owner: Bart Vanhoutem & Sanne Maertens
Website: www.rijwielwerkplaats-vanhoutem.be
Email: info@rijwielwerkplaats-vanhoutem.be
Phone number: +32471902386
Street adres: Kerkweg 64
9970 Oostmoere
Slogan/shop information: Herstellingen van alle merken.
Logo: see files.
Target Market(s)
People who seek a mechanic to fix or upgrade their bikes.
Contact Information for Business Card
Information:
Website: info@rijwielwerkplaats-vanhoutem.be
9970 Oostmoere
Logo: see files.

```html
<!DOCTYPE html>
<html lang="nl">
<head>
<meta charset="utf-8">
<title>Rijwielwerkplaats Vanhoutem – visitekaartje</title>
<link rel="stylesheet" href="https://fonts.googleapis.com/css2?family=Montserrat:wght@800&family=Open+Sans:wght@400;700&display=swap">
<style>
  :root {
    --backdrop: #2b2b2d;
    --ink: #111111;
    --card-white: #f7f7f7;
    --brand-red: #d81f45;
    --brand-red-dark: #b8163a;
    --soft-pink: #f3b6c4;
    --grey: #555555;
    --white: #ffffff;
  }
  * { margin: 0; padding: 0; box-sizing: border-box; }
  html, body {
    width: 1200px; height: 900px; overflow: hidden;
    background: var(--backdrop);
  }
  .canvas { position: relative; width: 1200px; height: 900px; }

  .card {
    position: absolute; width: 540px; height: 350px;
    border-radius: 4px; overflow: hidden;
    box-shadow: 0 14px 34px rgba(0,0,0,.45);
  }

  /* Back side */
  .card-back {
    left: 50px; top: 80px;
    background: var(--ink);
    border-bottom: 9px solid var(--brand-red);
    display: flex; flex-direction: column; align-items: center; justify-content: center;
  }
  .brand-dot {
    width: 46px; height: 46px; border-radius: 50%;
    background: var(--brand-red); margin-bottom: 18px;
  }
  .wordmark {
    font-family: "Montserrat", sans-serif; font-weight: 800;
    text-transform: uppercase; letter-spacing: 1px; line-height: 1.15;
  }
  .card-back .wordmark {
    color: var(--white); font-size: 27px; text-align: center;
  }

  /* Front side */
  .card-front { left: 610px; top: 440px; background: var(--card-white); }
  .front-top { position: absolute; inset: 0 0 160px 0; }
  .card-front .wordmark {
    position: absolute; right: 28px; top: 28px;
    color: var(--ink); font-size: 21px; text-align: right;
  }
  .owners { position: absolute; left: 30px; top: 108px; font-family: "Open Sans", sans-serif; }
  .owners-names {
    color: var(--brand-red); font-weight: 700; font-size: 17px;
    text-transform: uppercase; letter-spacing: .3px;
  }
  .owners-role { color: var(--grey); font-size: 13px; margin-top: 3px; }

  .tagline-band {
    position: absolute; left: 0; right: 0; top: 190px; height: 32px;
    background: var(--ink); color: var(--white);
    font-family: "Open Sans", sans-serif; font-size: 14px;
    display: flex; align-items: center; padding-left: 30px;
  }
  .contact-panel {
    position: absolute; left: 0; right: 0; top: 222px; bottom: 0;
    background: linear-gradient(180deg, var(--brand-red), var(--brand-red-dark));
    padding: 12px 30px;
    font-family: "Open Sans", sans-serif; font-size: 12.5px; line-height: 17px;
    color: var(--soft-pink);
  }
  .address { margin-bottom: 6px; }
  .contact-line { display: flex; align-items: center; gap: 9px; }
  .contact-line svg { width: 12px; height: 12px; flex: none; fill: var(--soft-pink); }
</style>
</head>
<body>
<main class="canvas">

  <section class="card card-back" aria-label="Achterkant visitekaartje">
    <div class="brand-dot"></div>
    <div class="wordmark">Rijwielwerkplaats<br>Vanhoutem</div>
  </section>

  <section class="card card-front" aria-label="Voorkant visitekaartje">
    <div class="front-top">
      <div class="wordmark">Rijwielwerkplaats<br>Vanhoutem</div>
      <div class="owners">
        <p class="owners-names">Bart Vanhoutem &amp; Sanne Maertens</p>
        <p class="owners-role">Shop owner</p>
      </div>
    </div>

    <div class="tagline-band">Herstellingen van alle merken</div>

    <div class="contact-panel">
      <p class="address">Kerkweg 64<br>9970 Oostmoere</p>
      <p class="contact-line">
        <svg viewBox="0 0 24 24" aria-hidden="true"><path d="M6.6 10.8a15.1 15.1 0 0 0 6.6 6.6l2.2-2.2c.3-.3.7-.4 1-.2 1.1.4 2.3.6 3.6.6.6 0 1 .4 1 1V20c0 .6-.4 1-1 1A17 17 0 0 1 3 4c0-.6.4-1 1-1h3.5c.6 0 1 .4 1 1 0 1.3.2 2.5.6 3.6.1.3 0 .7-.2 1z"/></svg>
        +32471902386
      </p>
      <p class="contact-line">
        <svg viewBox="0 0 24 24" aria-hidden="true"><path d="M2 5h20v14H2z M3.5 6.5 12 13l8.5-6.5" fill-rule="evenodd"/><path d="M2 5l10 8 10-8v2l-10 8L2 7z" fill="#b8163a"/></svg>
        info@rijwielwerkplaats-vanhoutem.be
      </p>
      <p class="contact-line">
        <svg viewBox="0 0 24 24" aria-hidden="true"><circle cx="12" cy="12" r="10"/><path d="M2 12h20M12 2c3 3 3 17 0 20M12 2c-3 3-3 17 0 20" stroke="#b8163a" stroke-width="1.6" fill="none"/></svg>
        www.rijwielwerkplaats-vanhoutem.be
      </p>
    </div>
  </section>

</main>
</body>
</html>
```